Web Design for Financial Consulting Company

We need a website design for a financial consulting company "Kelvane Consulting". We build financial models, scenario analysis, handle the budgeting process and provide temporary staffing. I have over 10 years of experience. My Excel expertise and analytical savvy has saved clients over $17 million in profit.

Target Market(s)

Small to medium businesses

Industry/Entity Type

Financial Consulting

Number of Pages Required

4 page

Requirements
Must have
• Professional looking
Nice to have
• A little futuristic looking

```html
<!DOCTYPE html>
<html lang="en">
<head>
<meta charset="utf-8">
<title>Kelvane Consulting</title>
<link href="https://fonts.googleapis.com/css2?family=Barlow:wght@400;500;600;700&family=Barlow+Condensed:wght@800&family=Roboto:wght@400;500;700&display=swap" rel="stylesheet">
<style>
:root{
  --navy:#0c3a5f;
  --navy-dark:#0b2c4b;
  --blue:#00aef0;
  --blue-soft:#e9f5fb;
  --text:#333a44;
  --muted:#555d66;
  --white:#ffffff;
}
*{box-sizing:border-box;margin:0;padding:0}
html,body{width:1200px;height:3168px;overflow:hidden;background:var(--white)}
body{font-family:"Roboto",Arial,sans-serif;color:var(--text)}
.canvas{position:relative;width:1200px;height:3168px;overflow:hidden}
.abs{position:absolute}
.heading{font-family:"Barlow",Arial,sans-serif;font-weight:500;color:var(--navy)}
.btn{position:absolute;display:flex;align-items:center;justify-content:center;background:var(--blue);color:var(--white);font:600 12px "Roboto",Arial,sans-serif;letter-spacing:.3px}

/* top bar */
.topbar{position:absolute;left:0;top:0;width:1200px;height:30px;background:var(--navy-dark);color:var(--white);font-size:10px}
.topbar .item{position:absolute;top:9px;display:flex;align-items:center;gap:6px}
.topbar .dot{position:absolute;top:8px;width:13px;height:13px;border-radius:50%;background:var(--white)}
.topbar .quote{position:absolute;left:970px;top:0;width:108px;height:30px;background:var(--blue);display:flex;align-items:center;justify-content:center;font:700 11px "Roboto",Arial,sans-serif;letter-spacing:.5px}

/* nav */
.nav{position:absolute;left:0;top:30px;width:1200px;height:55px;background:var(--white)}
.brand{position:absolute;display:flex;align-items:center;gap:8px;font-family:"Barlow",Arial,sans-serif;font-weight:700;color:var(--navy)}
.brand .mark{width:26px;height:26px;border:3px solid var(--blue)}
.nav .brand{left:123px;top:13px;font-size:21px}
.nav .link{position:absolute;top:20px;font:400 13px "Barlow",Arial,sans-serif;color:#333;letter-spacing:.3px}
.nav .link.active{color:var(--blue)}
.nav .phone{position:absolute;left:938px;top:17px;display:flex;align-items:center;gap:6px;font:400 14px "Barlow",Arial,sans-serif;color:#222}

/* hero */
.hero{position:absolute;left:0;top:85px;width:1200px;height:474px;background:linear-gradient(180deg,#2b4660 0%,#1b3550 45%,#0f2943 100%)}
.hero-title{position:absolute;left:674px;top:118px;font:500 49px/52px "Barlow",Arial,sans-serif;color:var(--white)}
.hero-title .accent{color:var(--blue)}
.hero-text{position:absolute;left:674px;top:300px;width:420px;font:400 13px/19px "Roboto",Arial,sans-serif;color:var(--white)}

/* feature band */
.band{position:absolute;left:0;top:559px;width:1200px;height:148px;background:var(--blue);color:var(--white)}
.band .circle{position:absolute;width:90px;height:90px;border-radius:50%;border:2px solid var(--white);display:flex;align-items:center;justify-content:center}
.band .circle .inner{width:72px;height:72px;border-radius:50%;background:var(--white);display:flex;align-items:center;justify-content:center}
.band .title{position:absolute;font:600 17px/21px "Barlow",Arial,sans-serif}
.band .square{position:absolute;left:562px;top:37px;width:76px;height:76px;border:5px solid var(--white)}

/* section labels */
.label{position:absolute;font:400 12px "Roboto",Arial,sans-serif;color:var(--blue);display:flex;align-items:center;gap:8px}
.label .line{display:inline-block;width:50px;height:1px;background:var(--blue)}
.label-icon{position:absolute;width:20px;height:20px;border:2px solid var(--blue)}

/* about */
.about h2{position:absolute;left:122px;top:826px;font-size:38px;line-height:41px}
.about .copy{position:absolute;left:122px;top:928px;width:420px;font-size:12.5px;line-height:20px;color:var(--text)}
.about ul{position:absolute;left:123px;top:1022px;list-style:none}
.about li{display:flex;align-items:center;gap:12px;height:26px;font:500 11.5px "Roboto",Arial,sans-serif;color:#1b1f24}
.about li::before{content:"";width:10px;height:10px;border-radius:50%;background:var(--navy)}
.photo{position:absolute}

/* services */
.services{position:absolute;left:0;top:1239px;width:1200px;height:605px;background:var(--blue-soft);overflow:hidden}
.ghost{position:absolute;left:0;top:498px;width:1200px;text-align:center;font:800 124px/1 "Barlow Condensed",Arial,sans-serif;color:var(--white);letter-spacing:2px;white-space:nowrap}
.card{position:absolute;top:1427px;width:223px;height:294px;background:var(--white)}
.card .img{position:absolute;left:0;top:0;width:100%;height:134px}
.card .icon{position:absolute;left:80px;top:100px;width:62px;height:62px;border-radius:50%;background:var(--blue);border:3px solid var(--white);display:flex;align-items:center;justify-content:center}
.card h3{position:absolute;left:0;top:174px;width:100%;text-align:center;font:600 17px "Barlow",Arial,sans-serif;color:var(--navy)}
.card p{position:absolute;left:14px;top:200px;width:195px;text-align:center;font-size:12px;line-height:16px;color:var(--muted)}
.arrow{position:absolute}

/* testimonials */
.tcard{position:absolute;top:2041px;width:460px;height:213px;background:var(--white);box-shadow:0 4px 24px rgba(12,58,95,.08)}
.tcard .avatar{position:absolute;left:34px;top:62px;width:110px;height:110px;border-radius:50%;border:2px solid var(--navy);padding:5px}
.tcard .avatar span{display:block;width:100%;height:100%;border-radius:50%;background:linear-gradient(160deg,#d9dde1,#8a96a3)}
.tcard .qbadge{position:absolute;left:68px;top:28px;width:42px;height:42px;border-radius:50%;background:var(--navy);color:var(--white);font:700 34px/52px Georgia,serif;text-align:center}
.tcard .name{position:absolute;left:166px;top:48px;font:400 14px "Roboto",Arial,sans-serif;color:var(--blue)}
.tcard p{position:absolute;left:165px;top:72px;width:270px;font-size:12px;line-height:17px;color:var(--muted)}

/* start */
.start h2{position:absolute;left:667px;top:2400px;font-size:38px;line-height:40px}
.start .copy{position:absolute;left:668px;top:2496px;width:410px;font-size:12.5px;line-height:20px}
.skill{position:absolute;left:668px;width:408px}
.skill .row{display:flex;justify-content:space-between;font:700 11px "Roboto",Arial,sans-serif;color:#1b1f24}
.skill .track{margin-top:12px;height:9px;background:#e8edf1}
.skill .fill{height:100%;background:var(--blue)}

/* newsletter */
.cta{position:absolute;left:0;top:2822px;width:1200px;height:156px;background:var(--blue)}
.cta h2{position:absolute;left:122px;top:38px;font:500 36px/41px "Barlow",Arial,sans-serif;color:var(--white)}
.cta .form{position:absolute;left:660px;top:57px;width:416px;height:48px;border:1px solid var(--white);display:flex}
.cta .field{flex:1;display:flex;align-items:center;padding-left:14px;font-size:11px;color:var(--white)}
.cta .submit{width:117px;background:var(--navy-dark);color:var(--white);display:flex;align-items:center;justify-content:center;font:700 13px "Roboto",Arial,sans-serif}

/* footer */
.footer{position:absolute;left:0;top:2978px;width:1200px;height:190px;background:var(--navy-dark);color:var(--white);font-size:10px}
.footer .brand{left:123px;top:30px;font-size:18px;color:var(--white)}
.footer .brand .mark{width:20px;height:20px}
.footer .contact{position:absolute;left:123px;display:flex;align-items:center;gap:7px}
.footer .ic{width:13px;height:13px;border-radius:50%;background:var(--white)}
.footer .divider{position:absolute;top:40px;width:1px;height:105px;background:rgba(255,255,255,.6)}
.footer h4{position:absolute;top:38px;font:500 15px "Barlow",Arial,sans-serif}
.footer .links{position:absolute;list-style:none}
.footer .links li{height:18.4px;font-size:9.5px}
.footer .social li{display:flex;align-items:center;gap:14px;height:21px;font-size:9.5px}
</style>
</head>
<body>
<div class="canvas">

  <!-- top bar -->
  <div class="topbar">
    <div class="item" style="left:123px">
      <svg width="13" height="9" viewBox="0 0 13 9"><rect x=".5" y=".5" width="12" height="8" fill="none" stroke="#fff"/><path d="M.5 .5l6 4.5 6-4.5" fill="none" stroke="#fff"/></svg>
      hello@kelvaneconsulting.com
    </div>
    <div class="item" style="left:409px">
      <svg width="10" height="13" viewBox="0 0 10 13"><path d="M5 0a5 5 0 0 0-5 5c0 4 5 8 5 8s5-4 5-8a5 5 0 0 0-5-5z" fill="#fff"/><circle cx="5" cy="5" r="2" fill="#0b2c4b"/></svg>
      410 Harbor Lane, Suite 1200, Millbrook, ST 40210
    </div>
    <span class="dot" style="left:855px"></span>
    <span class="dot" style="left:878px"></span>
    <span class="dot" style="left:903px"></span>
    <span class="dot" style="left:926px"></span>
    <div class="quote">GET A QUOTE</div>
  </div>

  <!-- navigation -->
  <div class="nav">
    <div class="brand"><span class="mark"></span>Kelvane Consulting</div>
    <span class="link active" style="left:382px">Home</span>
    <span class="link" style="left:472px">About</span>
    <span class="link" style="left:562px">Services</span>
    <span class="link" style="left:669px">Testimonial</span>
    <span class="link" style="left:788px">Contact Us</span>
    <div class="phone">
      <svg width="20" height="20" viewBox="0 0 20 20"><circle cx="10" cy="10" r="9" fill="none" stroke="#00aef0" stroke-width="1.6"/><path d="M7 5.5l1.6 2.4-1 1.2c.6 1.3 1.6 2.3 2.9 2.9l1.2-1 2.4 1.6-.9 1.9c-3.8-.2-7.2-3.6-7.4-7.4z" fill="#00aef0"/></svg>
      +1 (555) 014-2090
    </div>
  </div>

  <!-- hero -->
  <div class="hero" role="img" aria-label="Night city skyline with tall office towers under a dark blue tint"></div>
  <h1 class="hero-title" style="top:203px">Helping your<br><span class="accent">finance</span> team and<br>increasing profit</h1>
  <p class="hero-text" style="top:385px">We build financial models, scenario analysis, handle the budgeing process and provide temporary staffing.</p>

  <!-- feature band -->
  <div class="band">
    <div class="circle" style="left:123px;top:29px"><div class="inner">
      <svg width="40" height="40" viewBox="0 0 40 40"><path d="M17 6h6l-2 4h-2z" fill="#0c3a5f"/><circle cx="20" cy="17" r="8" fill="#0c3a5f"/><text x="20" y="21" text-anchor="middle" font-size="10" fill="#fff" font-family="Arial">$</text><path d="M4 30l8-4h8l4 2-6 1h-4l6 1 10-5 4 2-14 8H4z" fill="#00aef0"/></svg>
    </div></div>
    <div class="title" style="left:235px;top:26px">Solution Focused &amp; Customer<br>Benefited Financial Service</div>
    <div class="abs" style="left:253px;top:94px;font:700 12px 'Roboto',Arial,sans-serif">VIEW ALL SERVICES</div>
    <div class="square"></div>
    <div class="title" style="left:640px;top:26px;width:320px;text-align:right">Need Better Plan To Star Business?<br>Start with Kelvane Consulting</div>
    <div class="abs" style="left:809px;top:84px;width:150px;height:34px;border:1.5px solid #fff;display:flex;align-items:center;justify-content:center;font:700 12px 'Roboto',Arial,sans-serif">REQUEST A QUOTE</div>
    <div class="circle" style="left:985px;top:29px"><div class="inner">
      <svg width="40" height="40" viewBox="0 0 40 40"><circle cx="20" cy="15" r="8" fill="#0c3a5f"/><path d="M10 15a10 10 0 0 1 20 0" fill="none" stroke="#0c3a5f" stroke-width="2.5"/><rect x="8" y="13" width="4" height="7" rx="1" fill="#00aef0"/><rect x="28" y="13" width="4" height="7" rx="1" fill="#00aef0"/><path d="M8 36c0-7 5-11 12-11s12 4 12 11z" fill="#0c3a5f"/></svg>
    </div></div>
  </div>

  <!-- about -->
  <section class="about">
    <div class="label" style="left:123px;top:802px">About company <span class="line"></span></div>
    <h2 class="heading">About Kelvane<br>Consulting</h2>
    <p class="copy">I am an experienced Finance professional who develops strategic financial plans, provides insightful analysis, and supports decision-making. With over 10 years of experience, I have successfully increased profitability for clients by $17M</p>
    <ul>
      <li>Start Your Business with brainstorming</li>
      <li>The ability to identify market-entry</li>
      <li>Ensure to increase of expected sales</li>
    </ul>
    <div class="btn" style="left:123px;top:1115px;width:112px;height:37px">LEARN MORE</div>
    <div class="photo" style="left:658px;top:782px;width:424px;height:416px;background:linear-gradient(135deg,#8fb4cf 0%,#d8e3ea 45%,#f2b77a 70%,#00aef0 100%)" role="img" aria-label="Businesswoman reading a tablet against a bright city backdrop"></div>
  </section>

  <!-- services -->
  <div class="services">
    <div class="ghost">KELVANE CONSULTING</div>
  </div>
  <span class="label-icon" style="left:590px;top:1291px"></span>
  <div class="label" style="left:507px;top:1317px"><span class="line"></span>What We Do<span class="line"></span></div>
  <h2 class="heading abs" style="left:0;top:1343px;width:1200px;text-align:center;font-size:34px">Our Services</h2>

  <svg class="arrow" style="left:90px;top:1561px" width="14" height="26" viewBox="0 0 14 26"><path d="M12 2L2 13l10 11" fill="none" stroke="#0c3a5f" stroke-width="2"/></svg>
  <svg class="arrow" style="left:1093px;top:1561px" width="14" height="26" viewBox="0 0 14 26"><path d="M2 2l10 11L2 24" fill="none" stroke="#0c3a5f" stroke-width="2"/></svg>

  <div class="card" style="left:123px">
    <div class="img" role="img" aria-label="Model house, coins and banknotes on a desk" style="background:linear-gradient(135deg,#c9ccc8,#a49a86 60%,#6d6a66)"></div>
    <div class="icon"><svg width="30" height="30" viewBox="0 0 30 30" fill="none" stroke="#fff" stroke-width="1.6"><circle cx="15" cy="15" r="6"/><text x="15" y="19" text-anchor="middle" font-size="9" fill="#fff" stroke="none" font-family="Arial">$</text><circle cx="5" cy="5" r="2.5"/><circle cx="25" cy="5" r="2.5"/><circle cx="5" cy="25" r="2.5"/><circle cx="25" cy="25" r="2.5"/><path d="M7 7l4 4M23 7l-4 4M7 23l4-4M23 23l-4-4"/></svg></div>
    <h3>Financial Models</h3>
    <p>Financial analysis, scenario modeling, pricing analysis,</p>
  </div>
  <div class="card" style="left:366px">
    <div class="img" role="img" aria-label="Hands holding a tablet showing a budget screen" style="background:linear-gradient(135deg,#d8dadb,#b9bcbf 55%,#8d9094)"></div>
    <div class="icon"><svg width="30" height="30" viewBox="0 0 30 30" fill="none" stroke="#fff" stroke-width="1.6"><circle cx="15" cy="15" r="12"/><circle cx="15" cy="15" r="8"/><path d="M11 15l3 3 5-6"/></svg></div>
    <h3>Budgeting Process</h3>
    <p>Building budgets from scratch, revamping current process to be more robust and scalable.</p>
  </div>
  <div class="card" style="left:610px">
    <div class="img" role="img" aria-label="Office team reviewing documents together" style="background:linear-gradient(135deg,#eef0f2,#c6cbd1 50%,#7b8591)"></div>
    <div class="icon"><svg width="30" height="30" viewBox="0 0 30 30" fill="none" stroke="#fff" stroke-width="1.6"><circle cx="15" cy="7" r="5"/><path d="M12.5 7l2 2 3-3.5"/><circle cx="8" cy="18" r="3"/><circle cx="15" cy="18" r="3"/><circle cx="22" cy="18" r="3"/><path d="M3 28c0-3 2-5 5-5s5 2 5 5M10 28c0-3 2-5 5-5s5 2 5 5M17 28c0-3 2-5 5-5s5 2 5 5"/></svg></div>
    <h3>Temporary Staffing</h3>
    <p>Years of Financial Planning and Analysis experience across multiple industries can help temporary staffing needs.</p>
  </div>
  <div class="card" style="left:854px">
    <div class="img" role="img" aria-label="Piggy bank beside stacked wooden blocks with a rising arrow" style="background:linear-gradient(135deg,#eceae6,#d9c7a8 60%,#c19a6b)"></div>
    <div class="icon"><svg width="30" height="30" viewBox="0 0 30 30" fill="none" stroke="#fff" stroke-width="1.6"><circle cx="15" cy="15" r="8"/><path d="M15 2v4M15 24v4M2 15h4M24 15h4M6 6l3 3M21 21l3 3M24 6l-3 3M6 24l3-3"/><path d="M15 19v-8M12 14l3-3 3 3"/></svg></div>
    <h3>Process Improvement</h3>
    <p>Month endclose, reporting, budgeting.</p>
  </div>
  <div class="btn" style="left:525px;top:1755px;width:150px;height:37px">VIEW ALL SERVICES</div>

  <!-- testimonials -->
  <span class="label-icon" style="left:590px;top:1896px"></span>
  <div class="label" style="left:509px;top:1921px"><span class="line"></span>Testimonial<span class="line"></span></div>
  <h2 class="heading abs" style="left:0;top:1944px;width:1200px;text-align:center;font-size:37px">What Our Happy Clints Say</h2>

  <svg class="arrow" style="left:90px;top:2132px" width="14" height="26" viewBox="0 0 14 26"><path d="M12 2L2 13l10 11" fill="none" stroke="#0c3a5f" stroke-width="2"/></svg>
  <svg class="arrow" style="left:1093px;top:2132px" width="14" height="26" viewBox="0 0 14 26"><path d="M2 2l10 11L2 24" fill="none" stroke="#0c3a5f" stroke-width="2"/></svg>

  <div class="tcard" style="left:119px">
    <div class="avatar"><span role="img" aria-label="Portrait of client Daren Holt"></span></div>
    <div class="qbadge">&#8220;</div>
    <div class="name">Daren Holt</div>
    <p>Capitalize on low hanging fruit to identify a ballpark value added activity to beta test. Override the digital Nanotechnology immersion along the information divide with additional clickthroughs from DevOps highway.</p>
  </div>
  <div class="tcard" style="left:615px">
    <div class="avatar"><span role="img" aria-label="Portrait of client Mira Castell"></span></div>
    <div class="qbadge">&#8220;</div>
    <div class="name">Mira Castell</div>
    <p>Capitalize on low hanging fruit to identify a ballpark value added activity to beta test. Override the digital Nanotechnology immersion along the information divide with additional clickthroughs from DevOps highway.</p>
  </div>

  <!-- start section -->
  <section class="start">
    <div class="photo" style="left:122px;top:2305px;width:423px;height:467px;background:linear-gradient(160deg,#cfe0ee 0%,#7c93ab 45%,#2f4b68 75%,#00aef0 100%)" role="img" aria-label="Glass office tower seen from below against a pale sky"></div>
    <div class="label" style="left:668px;top:2374px">Let's Start <span class="line"></span></div>
    <h2 class="heading">Start Your Business with<br>Kelvane Consulting</h2>
    <p class="copy">I am an experienced Finance professional who develops strategic financial plans, provides insightful analysis, and supports decision-making.</p>
    <div class="skill" style="top:2557px"><div class="row"><span>Business</span><span>90%</span></div><div class="track"><div class="fill" style="width:89%"></div></div></div>
    <div class="skill" style="top:2609px"><div class="row"><span>Consulting</span><span>70%</span></div><div class="track"><div class="fill" style="width:76%"></div></div></div>
    <div class="skill" style="top:2662px"><div class="row"><span>Strategy</span><span>80%</span></div><div class="track"><div class="fill" style="width:86%"></div></div></div>
    <div class="btn" style="left:668px;top:2716px;width:110px;height:37px">GET STARTED</div>
  </section>

  <!-- newsletter -->
  <div class="cta">
    <h2>Solution Focused &amp; Customer<br>Benefited Financial Services</h2>
    <div class="form"><div class="field">Enter your Email</div><div class="submit">SIGN UP</div></div>
  </div>

  <!-- footer -->
  <footer class="footer">
    <div class="brand"><span class="mark"></span>Kelvane Consulting</div>
    <div class="contact" style="top:70px"><span class="ic"></span>hello@kelvaneconsulting.com</div>
    <div class="contact" style="top:96px"><span class="ic"></span>410 Harbor Lane, Suite 1200, Millbrook, ST 40210</div>
    <div class="contact" style="top:122px"><span class="ic"></span>Call Anytime +1 (555) 014-2090</div>
    <div class="abs" style="left:123px;top:153px;font-size:9px">© 2023 Kelvane Consulting All rights reserved.</div>
    <span class="divider" style="left:449px"></span>
    <span class="divider" style="left:824px"></span>
    <h4 style="left:616px">About Us</h4>
    <ul class="links" style="left:616px;top:66px">
      <li>Home</li><li>About</li><li>Services</li><li>Testimonial</li><li>Contact Us</li>
    </ul>
    <h4 style="left:1005px">Follow Us</h4>
    <ul class="links social" style="left:1006px;top:63px">
      <li><span class="ic"></span>Circlehub</li>
      <li><span class="ic"></span>Chatterly</li>
      <li><span class="ic"></span>Workgraph</li>
      <li><span class="ic"></span>Snapframe</li>
    </ul>
  </footer>

</div>
</body>
</html>
```